Nutritional & Gastrointestinal Health Consulting Service-Website design

We need a website design for a new health consulting service called "Bright Harbor" based in Perth, Australia.

We will be providing consulting services in the areas of:
1) Nutrition and Diet
2) Gastrointestinal Health (which means stomach & digestive system related health)

These consulting services will be provided by an Accredited Dietitian and a Paediatric Gastroenterologist.

We are open to creative ideas in terms of design, layout, fonts and colours. We also would love to see images of nature in the backdrop with families (adults with kids) having a good time, fresh fruits and vegetables displayed in a farmer's market or supermarket. 2 or 3 images should be sufficient. We would also definitely want our logo somewhere in the main page of website. The logo file is also attached. Please have a look at a website's design that we really liked. We would love to see designs inspired by that style. The website details are in the in the "nice to have priorities" section of this project brief.

We also would be looking at website designers with software coding skills so that if we like the design we can go ahead with the next step of coding.

The website design should communicate the purpose of the website and at the same time be simple, elegant and unique/eye-catching.

We look forward to receiving creative ideas for our website from you all. Good luck!
Updates

More details have been added to our project- for example: Logo, fonts style, must haves etc etc. Please view the updated project brief. Looking forward to receiving your fantastic ideas for our website. Thanking you

Hi, I have updated the colour preference. Will add the content preferences tomorrow. thanks

Hello all, I have now added a LOT more content to what we want in our website. It is very much in detail, so please carefully have a read through the entire project brief. If you have any questions write back to me and I will try to respond as quickly as I can. Last few days were busy so couldn't respond quickly to all of you who had send me designs/queries/questions. Thank you for your patience. I look forward to receiving fantastic designs from you all. Good Luck :-)

Target Market(s)

Adults based in western speaking countries aged 18 to 60 years

Industry/Entity Type

Software

Font styles to use
Sans Serif
Script

Colors
faa54b
acd036

Requirements
Must have
• The website must have the MAIN logo file attached. I have attached 3 files: 1) MAIN logo; 2) supplementary logo A ; 3) supplementary logo B

I have selected 2 colours from the colour scheme (see below)-(as the colour of our logo is that).
However we would also like to see LIGHT CHOCOLATE BROWN or CHOCOLATE BROWN colour used as the background colour of the website
Preferred WEBSITE CONTENT:
1) HOME PAGE:
Content required=
--Company Logo
--Dr Ravel Ostrin
Paediatric Gastroenterologist & Hepatologist
-Leora Ostrin.
Dietitian & Nutritionist
--Website Menu (either listed horizontally or vertically):
Once clicked on each name:

Under each of the Website Menu items we want the following Headings to be added

2) ABOUT US page:
Sub-heading under this: Qualification, Skills, Special Interest

3) SERVICES
RAVEL'S PAGE: Individual Consultation, Endoscopy procedures
Individual Consultation, Group Based Services, Food Diary, Food & Symptom Diary

4) FEES & REBATE: Content as below:
Please Note: Payment of full fees is required at the time of consultation and procedures. 48 hours notice is required for cancellation of appointments/non-attendance. Failure to provide this may result in a fee being incurred. Please call reception to find out the amount of fee charged for cancellation of appointments/non-attendance.
headings are:
Paediatric Gastroenterology:
Ravel's pge
Individual Consultation - Initial (upto 30 mins):
Review Consultation (upto 15 mins):
Endoscopy procedures - No Gap fees charged. Fees will be billed directly to Carewell. If any queries, please contact reception.

leora's pge
sub heading:
Individual Consultation - Initial (upto 45 mins):
Individual Consultation - Review (upto 30 mins):

Concession-Individual Consultation -Initial (upto 45 mins):
Concession-Individual Consultation - Review (upto 30 mins):
Please Note: Concession applies for health care card holders & pensioners

Group Based Services: Pricing subject to the type of service provided. Please contact us for an obligation free quote.
Education Topics Include:
- Paediatric Nutrition (Introducing Solids, Fussy Eating, Healthy Eating)
- Pregnancy Nutrition, Gestational Diabetes, Breastfeeding/Lactation Nutrition
- Healthy Eating, Supermarket Shopping Tips, Nutrition Label Reading Tips, Healthier
sub heading under nutrition & diet:
-Carewell:
--A rebate of $52.95 is available from Carewell if an EPC ( Enhanced Primary Care)/Chronic Disease Management (CDM) plan is issued by your GP.
--All mandatory paperwork needs to be available at the time of making your appointment for your eligibility.
-Private Health Fund:
--Most private health funds provide rebate on dietetic appointments. However the rebate amount depends on your level of cover. Thus, please contact your health fund to determine your entitled rebate.
-KRB: Approved provider for KRB services

6) FOR DOCTORS: Bright Harbor Paediatric Gastroenterologist Referral Form
Bright Harbor Dietitian Referral form
7) LOCATIONS & CONTACT

Paediatric Gastroenterology & Hepatology Service
Suite 82
Holloway Brenton Medical Centre
17 Quillan Fenwick Pde,
GLENDRA, WA 6177
P: (08) 9472 5031
F: (08) 9472 6640

Nutrition & Diet Service
Suite 82
17 Quillan Fenwick Pde,
GLENDRA, WA 6177
P: (08) 9472 5031
F: (08) 9472 6640

Tolliver Medical Centre
58-60 Corvane Parkway,
PELLARD, WA 6238
P: (08) 9627 4083
F: (08) 96274092
www.tmcpellard.com.au

This page should have a webform that has following titles:
-Your Name
-Your Email
-Your Phone
-Message

8) NEWS & BLOG
Nice to have
• We liked the design style of the websites below:
https://www.vivoraclinic.example/

http://tummywise.example/

But feel free to use your creativity too
Should not have
• Please do not use any body building or muscle building images

```html
<!DOCTYPE html>
<html lang="en">
<head>
<meta charset="utf-8">
<title>Bright Harbor – Contact</title>
<link href="https://fonts.googleapis.com/css2?family=Open+Sans:wght@300;400;700&display=swap" rel="stylesheet">
<style>
  :root{
    --orange:#faa54b;
    --orange-deep:#e3934a;
    --brown:#4a2a1e;
    --white:#ffffff;
    --line:#fde0bd;
    --map-land:#e6e2da;
    --map-water:#b3cff5;
  }
  *{box-sizing:border-box;margin:0;padding:0}
  html,body{width:1142px;height:1200px;overflow:hidden}
  body{background:var(--orange);font-family:"Open Sans",sans-serif;color:var(--brown);position:relative}
  .side-btn{position:absolute;top:85px;width:45px;height:45px;background:var(--orange-deep);display:flex;align-items:center;justify-content:center;color:var(--line)}
  .side-btn.menu{left:0}
  .side-btn.close{right:0;font-size:12px}
  .page-title{position:absolute;top:84px;left:0;width:100%;text-align:center;color:var(--white);font-weight:700;font-size:15px;letter-spacing:.3px}
  .rule{position:absolute;top:160px;left:49px;width:1042px;border-top:1px dashed var(--line)}
  .hero-box{position:absolute;left:419px;top:205px;width:303px;height:71px;border:1px solid var(--line);display:flex;align-items:center;justify-content:center;font-size:37px;font-weight:300;letter-spacing:.5px}
  .hero-box b{font-weight:700;margin-right:10px}
  .tagline{position:absolute;top:289px;width:100%;text-align:center;font-size:19px;font-weight:300}
  .intro{position:absolute;top:334px;left:316px;width:510px;text-align:center;font-family:Arial,sans-serif;font-size:12.6px;line-height:17.8px}
  .intro .hl{color:var(--white)}
  .section-title{position:absolute;width:100%;text-align:center;font-size:29px;font-weight:300;letter-spacing:-.3px}
  .section-title b{font-weight:700}
  .address{position:absolute;left:437px;top:513px;width:268px;height:89px;border:1px dashed var(--line);text-align:center;font-size:14.5px;font-weight:300;line-height:18px;padding-top:17px}
  .address .mail{color:var(--white)}
  .field{position:absolute;top:700px;height:45px;background:var(--orange-deep);color:var(--line);font-size:12.5px;padding:16px 13px}
  .send{position:absolute;top:700px;left:905px;width:188px;height:45px;background:var(--white);border-bottom:4px solid #e5e5e5;display:flex;align-items:center;justify-content:center;font-size:17px;font-weight:300;color:var(--brown)}
  .map{position:absolute;left:49px;top:843px;width:1044px;height:312px;background:linear-gradient(100deg,var(--map-water) 0%,#cbd9e8 22%,var(--map-land) 38%,var(--map-land) 100%)}
</style>
</head>
<body>
  <div class="side-btn menu" aria-label="Menu">
    <svg width="12" height="10" viewBox="0 0 12 10"><rect width="12" height="2" fill="#fde0bd"/><rect y="4" width="12" height="2" fill="#fde0bd"/><rect y="8" width="12" height="2" fill="#fde0bd"/></svg>
  </div>
  <div class="side-btn close" aria-label="Close">×</div>
  <h1 class="page-title">CONTACT</h1>
  <div class="rule"></div>

  <div class="hero-box"><b>CONTACT</b> US</div>
  <p class="tagline">we are specialized in gut health</p>
  <p class="intro">Bright Harbor offers consulting in nutrition and diet and in <span class="hl">digestive health</span>, led by an accredited dietitian and a paediatric gastroenterologist working side by side. Call reception or send us a message below to book an individual consultation, ask about group sessions or request a <b>referral form</b>. We usually reply within one business day and are happy to help.</p>

  <h2 class="section-title" style="top:458px">WE ARE <b>HERE</b></h2>
  <div class="address">
    Suite 82, 17 Quillan Fenwick Pde<br>
    (08) 9472 5031<br>
    <span class="mail">support@brightharbor.example</span>
  </div>

  <h2 class="section-title" style="top:645px">EMAIL <b>US</b></h2>
  <div class="field" style="left:49px;width:276px">Name</div>
  <div class="field" style="left:334px;width:277px">Mail</div>
  <div class="field" style="left:620px;width:276px">Message</div>
  <div class="send">Send Message</div>

  <h2 class="section-title" style="top:787px">ON THE <b>MAP</b></h2>
  <div class="map" role="img" aria-label="Street map showing the clinic location in Glendra"></div>
</body>
</html>
```